Brookvale Insurance Services - Insurance Agency Wesbite

I need a website for my insurance agency called Brookvale Insurance Services. I have attached my company logo. You can use the colors from the copy logo to create the website color scheme. I need a Request A Quote section.
Business Address: 7316 Marlowe Ave Unit D, Studio City Ca 91607
Business Phone: (818) 555-0193
I would need the following drop downs on the main page:

1st drop down:
Business Insurance
⁃ Commercial Auto
⁃ Employment Practice Liability Insurance
⁃ General Liability Insurance
⁃ Professional Liability Insurance
⁃ Property Insurance
⁃ Workers Compensation Insurance

2nd drop down:
Industries We Serve
- Construction
- Janitorial
- Landscapers
- Trucking
- ParcelWay Independent Service Providers (ISP)
Healthcare Industry
- Community Care Facilities
- Home Health Agencies
- Hospice
- Nursing Homes

3rd drop down:
Risk Management
- Claims Management
- Compliance & Risk Management

4th drop down
Request a quote

5th drop down
About Us

6th drop down
Contact US

Target Market(s)

Potential clients

Industry/Entity Type

Business Insurance

Coding

Coded - Design and coding required

Number of Pages Required

5+ page

Colors
0054AA
0677BA
7BADD7
CADEEF
E8F1F8
00AB8E
00BBA5
67D7C9
C6EFE9
E9F9F6

Requirements
Must have
• Home Business Insurance - Commercial Auto - Employment Practice Liability Insurance - General Liability Insurance - Professional Liability Insurance - Property Insurance - Workers Compensation Insurance Industries We Serve - Construction - Janitorial - Landscapers - Manufacturing Companies - Restaurants - Towing - Trucking Healthcare Industry - Community Care Facilities - Home Health Agencies - Hospice - Nursing Homes - Risk Management - Claims Management - Compliance & Risk Management Request a Quote About Us Contact Us

```html
<!DOCTYPE html>
<html lang="en">
<head>
<meta charset="utf-8">
<title>Brookvale Insurance Services – Landing Page Mobile View</title>
<link href="https://fonts.googleapis.com/css2?family=Roboto:wght@400;500;700&display=swap" rel="stylesheet">
<style>
:root{
  --stage:#8296c0;
  --navy:#002a80;
  --green:#00962e;
  --ink:#111418;
  --hero:#e1e7ef;
  --paper:#ffffff;
  --footer:#040b1e;
  --line:#9aa8cf;
  --photo-warm:#b9a895;
  --photo-cool:#8f99a6;
}
*{margin:0;padding:0;box-sizing:border-box}
html,body{width:1200px;height:1200px;overflow:hidden;background:var(--stage)}
body{font-family:"Roboto",sans-serif;color:var(--ink)}
.board{position:absolute;left:0;top:0;width:1932px;height:1932px;transform:scale(.6211);transform-origin:0 0}
.screen{position:absolute;background:var(--paper);border-radius:40px;overflow:hidden}
.abs{position:absolute}
.nowrap{white-space:nowrap}
.photo{position:absolute}
.warm{background:linear-gradient(150deg,#d9d2c8,var(--photo-warm) 55%,#5d5650)}
.cool{background:linear-gradient(160deg,#c9cdd2,var(--photo-cool) 60%,#4a4f58)}
.band{position:absolute;background:var(--green)}
.btn{position:absolute;background:var(--navy);color:#fff;font-size:15px;display:flex;align-items:center;justify-content:center}
.brand{font-weight:700;color:var(--navy);letter-spacing:.5px}

/* screen 1 */
.s1{left:68px;top:65px;width:347px;height:1810px}
.s1 .hero-bg{left:0;top:88px;width:347px;height:459px;background:var(--hero)}
.s1 h1{left:22px;top:118px;font-size:34px;font-weight:500;line-height:38px}
.s1 .lead{left:22px;top:263px;font-size:14px;line-height:17.5px}
.s1 h2{left:22px;top:1376px;font-size:31px;font-weight:500;line-height:35px}
.s1 .body{left:22px;top:1462px;font-size:15px;line-height:22px}
.checks{left:22px;top:1610px;list-style:none;font-size:15px}
.checks li{display:flex;align-items:center;gap:10px;height:33px}

/* screen 2 */
.s2{left:458px;top:65px;width:347px;height:1465px;text-align:center}
.stat{position:absolute;left:0;width:347px;color:var(--green);font-weight:700;font-size:44px}
.stat small{font-size:29px}
.label{position:absolute;left:0;width:347px;font-size:15px}
.s2 h2{left:0;width:347px;top:593px;font-size:30px;font-weight:500;line-height:35px}
.tabbox{left:119px;top:721px;width:110px;height:109px;border:1px solid var(--navy)}
.tabname{left:0;width:347px;top:790px;font-size:19px;color:var(--navy);text-align:center}
.tabname span{background:var(--paper);padding:0 4px}
.card{left:23px;top:1212px;width:302px;height:164px;background:#fff;box-shadow:0 2px 12px rgba(0,0,0,.12);text-align:left;padding:22px 14px}
.card b{display:block;font-size:14px;margin-bottom:18px;font-weight:500}
.card p{font-size:12px;line-height:15px}
.card a{display:inline-block;margin-top:14px;font-size:12.5px;color:var(--navy)}
.pager{left:0;width:347px;top:1405px;font-size:17px;color:var(--navy);word-spacing:10px}

/* screen 3 */
.s3{left:848px;top:65px;width:347px;height:1395px}
.s3 h2{left:23px;top:475px;font-size:30px;font-weight:700;line-height:35px}
.tabs{left:23px;top:567px;width:302px;height:54px;border-bottom:2px solid var(--line);display:flex;font-size:13px}
.tabs .on{width:132px;background:var(--navy);color:#fff;display:flex;align-items:center;gap:14px;padding-left:16px;line-height:15px}
.tabs .off{display:flex;align-items:center;gap:16px;padding-left:30px}
.field{position:absolute;left:23px;width:302px;height:54px;border:1px solid var(--line);padding-left:18px;display:flex;align-items:center;font-size:15px;color:#666}
.contact{left:0;top:1065px;width:347px;height:330px;background:var(--navy);color:#fff}
.contact h3{position:absolute;left:0;width:347px;top:58px;text-align:center;font-size:30px;font-weight:700}
.row{position:absolute;left:25px;display:flex;gap:17px;align-items:flex-start;font-size:15px;line-height:17.5px;white-space:nowrap}

/* screen 4 */
.s4{left:1238px;top:65px;width:349px;height:1045px;background:var(--footer);color:#fff}
.s4 .brand{left:23px;top:78px;font-size:28px;color:#fff}
.s4 .mail{left:23px;top:155px;width:274px;height:38px;border-bottom:1px solid #aab;padding-left:15px;font-size:15px;color:#aab}
.sub{left:23px;top:201px;width:86px;height:32px;background:var(--green);font-size:13px;display:flex;align-items:center;justify-content:center}
.menu{left:23px;list-style:none;font-size:15px;line-height:17.5px;white-space:nowrap}
.menu .h{font-weight:700;margin-bottom:14px}
.menu li{margin-bottom:7.5px}
.menu .u{text-decoration:underline}

.bigname{left:1200px;top:1560px;width:600px;font-size:62px;line-height:68px;font-weight:700;color:var(--navy);white-space:nowrap}
.title{left:1058px;top:1765px;font-size:60px;color:#fff;font-weight:400;white-space:nowrap}
</style>
</head>
<body>
<div class="board">

  <!-- Screen 1: hero -->
  <section class="screen s1">
    <div class="abs brand" style="left:22px;top:32px;font-size:18px">Brookvale</div>
    <svg class="abs" style="left:298px;top:32px" width="24" height="18" viewBox="0 0 24 18"><path d="M1 2h22M1 9h22M1 16h22" stroke="#002a80" stroke-width="2.2"/></svg>
    <div class="abs hero-bg"></div>
    <div class="band" style="left:0;top:547px;width:347px;height:206px"></div>
    <h1 class="abs nowrap">Tailored Insurance<br>for Your Every Life<br>Chapter.</h1>
    <p class="abs lead nowrap">At the heart of our insurance services is a<br>commitment to security, offering personalized<br>coverage that evolves with your changing<br>needs.</p>
    <div class="btn" style="left:22px;top:362px;width:169px;height:54px">Request A Quote</div>
    <div class="photo warm" style="left:22px;top:446px;width:303px;height:357px" role="img" aria-label="Advisor shaking hands with a young couple"></div>
    <div class="abs" style="left:3px;top:923px;width:297px;height:392px;border:1px solid var(--green)"></div>
    <div class="photo cool" style="left:22px;top:942px;width:303px;height:405px" role="img" aria-label="Agent reviewing papers with an older client"></div>
    <h2 class="abs nowrap">Crafting a Protected<br>Path for Your Journey</h2>
    <p class="abs body nowrap">Experience the difference of insurance with a<br>human touch. Our company is dedicated to<br>understanding your unique needs, offering<br>responsive service, and delivering peace of<br>mind through thoughtful and comprehensive<br>coverage.</p>
    <ul class="abs checks">
      <li><svg width="18" height="12" viewBox="0 0 18 12"><path d="M1 7l3 3 6-8M7 9l1 1 6-8" fill="none" stroke="#002a80" stroke-width="1.4"/></svg>Financial Security</li>
      <li><svg width="18" height="12" viewBox="0 0 18 12"><path d="M1 7l3 3 6-8M7 9l1 1 6-8" fill="none" stroke="#002a80" stroke-width="1.4"/></svg>Tailored Coverage</li>
      <li><svg width="18" height="12" viewBox="0 0 18 12"><path d="M1 7l3 3 6-8M7 9l1 1 6-8" fill="none" stroke="#002a80" stroke-width="1.4"/></svg>Asset Protection</li>
    </ul>
    <div class="btn" style="left:22px;top:1715px;width:133px;height:54px">Learn more</div>
  </section>

  <!-- Screen 2: stats and services -->
  <section class="screen s2">
    <div class="stat" style="top:38px">123</div>
    <div class="label" style="top:111px">Projects Completed</div>
    <div class="stat" style="top:176px">$4.5 <small>billion</small></div>
    <div class="label" style="top:248px">Insurance Payouts</div>
    <div class="stat" style="top:313px">100%</div>
    <div class="label" style="top:385px">Claim Success Rate</div>
    <h2 class="abs">Wide Range of<br>Tailored Insurance<br>Services</h2>
    <div class="abs tabbox"></div>
    <svg class="abs" style="left:160px;top:742px" width="28" height="24" viewBox="0 0 28 24"><rect x="9" y="1" width="10" height="5" fill="none" stroke="#002a80" stroke-width="2"/><rect x="1" y="5" width="26" height="18" rx="2" fill="#002a80"/><rect x="12" y="11" width="4" height="4" fill="#fff"/></svg>
    <div class="abs tabname"><span>Business Insurance</span></div>
    <svg class="abs" style="left:32px;top:766px" width="12" height="20" viewBox="0 0 12 20"><path d="M10 2L2 10l8 8" fill="none" stroke="#555" stroke-width="2"/></svg>
    <svg class="abs" style="left:304px;top:766px" width="12" height="20" viewBox="0 0 12 20"><path d="M2 2l8 8-8 8" fill="none" stroke="#002a80" stroke-width="2"/></svg>
    <div class="band" style="left:4px;top:922px;width:343px;height:181px"></div>
    <div class="photo cool" style="left:23px;top:860px;width:302px;height:322px" role="img" aria-label="Two colleagues signing documents at a desk"></div>
    <div class="abs card">
      <b>Commercial Auto</b>
      <p class="nowrap">Lorem ipsum dolor sit amet consectetur. Id<br>pretium eget nunc magna sagittis lacus dui<br>tortor. Orci semper integer nec ut nisi elit<br>augue. Nunc egestas.</p>
      <a><u>Learn More</u> &nbsp;→</a>
    </div>
    <div class="abs pager"><u>1</u> 2 3 4 5 6</div>
  </section>

  <!-- Screen 3: quote form and contact -->
  <section class="screen s3">
    <div class="band" style="left:23px;top:86px;width:271px;height:77px"></div>
    <div class="photo warm" style="left:83px;top:125px;width:242px;height:297px" role="img" aria-label="Family of four standing together at home"></div>
    <h2 class="abs nowrap">Get A Quote To Get<br>Started!</h2>
    <div class="abs tabs">
      <div class="on"><svg width="18" height="16" viewBox="0 0 18 16"><rect x="6" y="1" width="6" height="4" fill="none" stroke="#fff" stroke-width="1.6"/><rect x="1" y="4" width="16" height="11" rx="1.5" fill="#fff"/></svg><span>Business<br>Insurance</span></div>
      <div class="off"><svg width="20" height="18" viewBox="0 0 20 18"><path d="M1 17V1h11v16M12 6h7v11M0 17h20M4 4h2M8 4h2M4 8h2M8 8h2M4 12h2M8 12h2M15 10h2M15 13h2" fill="none" stroke="#002a80" stroke-width="1.6"/></svg>Industries</div>
    </div>
    <div class="field" style="top:650px">Full name</div>
    <div class="field" style="top:719px">Email</div>
    <div class="field" style="top:788px;color:#222;justify-content:space-between;padding-right:22px">Select insurance type
      <svg width="12" height="8" viewBox="0 0 12 8"><path d="M1 1l5 5 5-5" fill="none" stroke="#222" stroke-width="1.6"/></svg></div>
    <div class="btn" style="left:23px;top:873px;width:171px;height:54px">Get A Quote Now</div>
    <div class="abs contact">
      <h3>Contact Us</h3>
      <div class="row" style="top:125px"><svg width="20" height="26" viewBox="0 0 20 26"><path d="M10 1a9 9 0 0 0-9 9c0 7 9 15 9 15s9-8 9-15a9 9 0 0 0-9-9z" fill="#fff"/><circle cx="10" cy="10" r="3.5" fill="#002a80"/></svg><span>7316 Marlowe Ave Unit D, Studio City Ca<br>91607</span></div>
      <div class="row" style="top:190px"><svg width="24" height="24" viewBox="0 0 24 24"><path d="M5 2l4 1 1 5-3 2c1 3 4 6 7 7l2-3 5 1 1 4c0 2-2 3-4 3C10 22 2 14 2 6c0-2 1-4 3-4z" fill="#fff"/></svg><span style="margin-top:3px">(818) 555-0193</span></div>
      <div class="row" style="top:251px"><svg width="26" height="20" viewBox="0 0 26 20"><rect x="1" y="1" width="24" height="18" rx="1.5" fill="#fff"/><path d="M2 3l11 8 11-8" fill="none" stroke="#002a80" stroke-width="2"/></svg><span>email@company.com</span></div>
    </div>
  </section>

  <!-- Screen 4: footer menu -->
  <section class="screen s4">
    <div class="abs brand">Brookvale</div>
    <div class="abs mail" style="display:flex;align-items:center">enter email address</div>
    <div class="abs sub">Subscribe</div>
    <ul class="abs menu" style="top:264px">
      <li class="h">Business Insurance</li>
      <li>Commercial Auto</li>
      <li class="u">Employment Practice Liability<br>Insurance</li>
      <li>General Liability Insurance</li>
      <li>Professional Liability<br>Insurance</li>
      <li>Property Insurance</li>
      <li>Workers Compensation<br>Insurance</li>
    </ul>
    <ul class="abs menu" style="top:520px">
      <li class="h">Industries</li>
      <li>Construction</li>
      <li class="u">Janitorial</li>
      <li>Landscapers</li>
      <li>Manufacturing Companies</li>
      <li>Restaurants</li>
      <li>Towing</li>
      <li>Trucking</li>
    </ul>
    <ul class="abs menu" style="top:748px">
      <li class="h">Healthcare Industry</li>
      <li>Community Care Facilities</li>
      <li class="u">Home Health Agencies</li>
      <li>Hospice</li>
      <li>Nursing Homes</li>
    </ul>
    <ul class="abs menu" style="top:902px">
      <li class="h">Risk Management</li>
      <li>Claims Management</li>
      <li class="u">Compliance &amp; Risk<br>Management</li>
    </ul>
  </section>

  <div class="abs bigname">Brookvale<br>Insurance Services</div>
  <div class="abs title">Landing Page Mobile View</div>
</div>
</body>
</html>
```